Visitenkarte erstellen für Reiki Praxis

Visitenkarten für Reiki Praxis Doppelseitig

business cards reiki practice double-sided

The background can also be a different color

```html
<!DOCTYPE html>
<html lang="en">
<head>
<meta charset="utf-8">
<title>Lumen Vitalis – Business Card</title>
<link href="https://fonts.googleapis.com/css2?family=Quicksand:wght@400;500;600&display=swap" rel="stylesheet">
<style>
  :root {
    --page-bg: #2a2c30;
    --card-bg: #2f2f31;
    --card-edge: #1c1c1e;
    --text-light: #d9d9d9;
    --text-muted: #bdbdbd;
    --accent-gold: #b9a35a;
    --accent-bronze: #a88a55;
    --accent-pink: #e0468f;
  }
  * { margin: 0; padding: 0; box-sizing: border-box; }
  html, body {
    width: 1200px;
    height: 1000px;
    overflow: hidden;
    background: var(--page-bg);
    font-family: "Quicksand", sans-serif;
  }
  .sheet {
    position: relative;
    width: 1200px;
    height: 1000px;
  }
  .card {
    position: absolute;
    left: 250px;
    width: 700px;
    height: 400px;
    background: var(--card-bg);
    border-radius: 4px;
    box-shadow: 0 6px 0 var(--card-edge), 0 16px 30px rgba(0,0,0,0.35);
  }
  .card--front { top: 70px; }
  .card--back { top: 530px; }

  /* Front side */
  .brand {
    position: absolute;
    top: 62px;
    left: 0;
    width: 100%;
    text-align: center;
  }
  .brand__mark {
    display: block;
    margin: 0 auto 16px;
    width: 56px;
    height: 56px;
  }
  .brand__name {
    font-size: 30px;
    font-weight: 500;
    letter-spacing: 1px;
    color: var(--text-light);
    text-transform: uppercase;
  }
  .brand__person {
    margin-top: 6px;
    font-size: 17px;
    font-weight: 500;
    letter-spacing: 6px;
    color: var(--accent-gold);
    text-transform: uppercase;
  }
  .contact {
    position: absolute;
    right: 44px;
    top: 196px;
    text-align: right;
    font-size: 15px;
    line-height: 1.35;
    color: var(--text-muted);
    list-style: none;
  }
  .address {
    position: absolute;
    left: 44px;
    bottom: 40px;
    font-style: normal;
    font-size: 15px;
    line-height: 1.35;
    color: var(--text-muted);
  }

  /* Back side */
  .emblem {
    position: absolute;
    top: 50%;
    left: 50%;
    transform: translate(-50%, -50%);
    display: flex;
    flex-direction: column;
    align-items: center;
    gap: 18px;
  }
  .emblem__circle {
    width: 150px;
    height: 150px;
  }
  .emblem__name {
    font-size: 24px;
    font-weight: 500;
    letter-spacing: 2px;
    color: var(--accent-pink);
    text-transform: uppercase;
  }
</style>
</head>
<body>
<main class="sheet">
  <section class="card card--front" aria-label="Business card front">
    <header class="brand">
      <svg class="brand__mark" viewBox="0 0 56 56" aria-hidden="true">
        <circle cx="28" cy="28" r="26" fill="none" stroke="var(--accent-bronze)" stroke-width="1.5"/>
      </svg>
      <h1 class="brand__name">Lumen Vitalis</h1>
      <p class="brand__person">Mira Estlund</p>
    </header>
    <ul class="contact">
      <li>+49 01234 56 78 90</li>
      <li>mira@lumenvitalis.com</li>
      <li>lumenvitalis.com</li>
    </ul>
    <address class="address">
      Lindenweg 7<br>
      Musterstadt<br>
      Germany
    </address>
  </section>

  <section class="card card--back" aria-label="Business card back">
    <div class="emblem">
      <svg class="emblem__circle" viewBox="0 0 150 150" aria-hidden="true">
        <circle cx="75" cy="75" r="72" fill="none" stroke="var(--accent-pink)" stroke-width="2"/>
      </svg>
      <p class="emblem__name">Lumen Vitalis</p>
    </div>
  </section>
</main>
</body>
</html>
```